Quillmere Financial Plans

I am looking for a complete resdesign of my small financial presentation. This is a Word Doc/PDF that I print off when meeting with people in private. I often present my "two pager" that I have been using for years and years. It tells them the basics of what I do, how I help people and foundational financial principles.

I have recently gone out on my own in business and have completely rebranded. This presentation is my most used tool, so it is the first of many things I would like to redo. I am hoping it will somehow coordinate with the colors of my business, not necessarily the EXACT same 3 colors everywhere, but have the design colors compliment.

I've uploaded all my logo designs, as well as the current "two-pager". I am not against it going to 3 pages if needed. As it will still land on 2 pages with duplex printing.

It has always been VERY simple. I am wanting it built into a more professional and design specific format, to show off my branding, without being over cluttered.

I am completely open to ANY graphics changes. Obviously some are very novice, the house on the last page has always been overly simplified.

```html
<!DOCTYPE html>
<html lang="en">
<head>
<meta charset="utf-8">
<title>Quillmere Financial Plans — Rule of 72 &amp; Taxes</title>
<link rel="stylesheet" href="https://fonts.googleapis.com/css2?family=Archivo:wght@400;500;600;700;800&display=swap">
<style>
  :root {
    --navy: #111e30;
    --navy-soft: #1c2d45;
    --green: #00ad3d;
    --green-deep: #008f33;
    --row-grey: #f2f4f3;
    --panel-grey: #f3f4f4;
    --line-grey: #d9dcdc;
    --ink: #111111;
    --muted: #3a4452;
    --alert-red: #e4090f;
    --white: #ffffff;
  }
  * { box-sizing: border-box; margin: 0; padding: 0; }
  html, body { width: 900px; height: 1200px; overflow: hidden; background: var(--white); }
  body { font-family: "Archivo", Arial, sans-serif; color: var(--ink); }
  .page { position: relative; width: 900px; height: 1200px; }

  /* Brand */
  .brand {
    position: absolute; right: 40px; top: 26px;
    display: flex; align-items: center; gap: 8px;
    font-size: 16px; font-weight: 700; color: var(--navy); letter-spacing: 0.2px;
  }
  .brand-mark { width: 10px; height: 10px; background: var(--green); }

  /* Section headings */
  .section-bar {
    position: absolute; left: 0; width: 500px; height: 46px;
    background: var(--navy); color: var(--white);
    font-size: 23px; font-weight: 800; letter-spacing: 0.6px;
    padding-left: 40px; display: flex; align-items: center;
  }
  .section-bar::after {
    content: ""; position: absolute; right: 0; top: 0; width: 8px; height: 100%;
    background: var(--green);
  }
  .section-bar.rule72 { top: 78px; }
  .section-bar.taxes { top: 530px; }

  /* Rule of 72 cards */
  .rate-grid {
    position: absolute; left: 40px; top: 150px; width: 810px;
    display: grid; grid-template-columns: repeat(4, 1fr); gap: 14px;
  }
  .rate-card {
    display: flex; flex-direction: column;
    border: 1px solid var(--line-grey); background: var(--white);
  }
  .rate-card .head {
    display: flex; justify-content: space-between; align-items: center;
    height: 38px; padding: 0 14px; background: var(--navy); color: var(--white);
    font-size: 13px; font-weight: 700; letter-spacing: 0.8px;
  }
  .rate-card .head .rate { font-size: 17px; font-weight: 800; color: var(--green); letter-spacing: 0; }
  .rate-card .rows { height: 224px; }
  .rate-card .row {
    display: flex; justify-content: space-between; align-items: center;
    height: 32px; padding: 0 14px; font-size: 14px; font-weight: 700;
  }
  .rate-card .row:nth-child(odd) { background: var(--row-grey); }
  .rate-card .row .age { color: var(--muted); font-weight: 600; }
  .rate-card .row:last-child .amount { color: var(--green-deep); }
  .rate-card .note {
    height: 48px; background: var(--green); color: var(--white);
    display: flex; flex-direction: column; justify-content: center; text-align: center;
    font-size: 12px; font-weight: 800; line-height: 15px; letter-spacing: 0.5px;
  }

  /* Taxes house */
  .roof { position: absolute; left: 40px; top: 598px; }

  .pillars {
    position: absolute; left: 40px; top: 676px; width: 810px; height: 288px;
    display: grid; grid-template-columns: repeat(4, 1fr); gap: 14px;
  }
  .pillar {
    display: flex; flex-direction: column; align-items: center;
    background: var(--panel-grey); border-top: 4px solid var(--green);
    padding: 22px 12px 18px; text-align: center;
  }
  .pillar-title { font-size: 17px; font-weight: 800; letter-spacing: 0.6px; color: var(--navy); margin-bottom: 16px; }
  .pillar-points { list-style: none; display: flex; flex-direction: column; gap: 14px; flex: 1; }
  .pillar-points li {
    font-size: 12px; font-weight: 500; line-height: 16px; text-transform: uppercase; color: var(--muted);
  }
  .verdict {
    width: 100%; padding-top: 14px; border-top: 1px solid #a7adb3;
    font-size: 18px; font-weight: 800; color: var(--alert-red); letter-spacing: 0.3px;
  }

  .foundation {
    position: absolute; left: 40px; top: 978px; width: 810px; height: 72px;
    background: var(--green); color: var(--white);
    display: grid; grid-template-columns: 1fr 1fr;
  }
  .foundation .col { display: grid; grid-template-rows: 1fr 1fr; }
  .foundation .col + .col { border-left: 1px solid rgba(255,255,255,0.55); }
  .foundation span {
    display: flex; align-items: center; justify-content: center;
    font-size: 15.5px; font-weight: 800; letter-spacing: 0.6px;
  }
  .foundation span:first-child { border-bottom: 1px solid rgba(255,255,255,0.55); }
</style>
</head>
<body>
<main class="page">
  <div class="brand"><span class="brand-mark"></span>Quillmere Financial Plans</div>

  <h2 class="section-bar rule72">RULE OF 72</h2>

  <section class="rate-grid">
    <div class="rate-card">
      <div class="head"><span>AGE</span><span class="rate">4%</span></div>
      <div class="rows">
        <div class="row"><span class="age">29</span><span class="amount">$10,000</span></div>
        <div class="row"><span class="age">47</span><span class="amount">$20,000</span></div>
        <div class="row"><span class="age">65</span><span class="amount">$40,000</span></div>
      </div>
      <div class="note"><span>MONEY DOUBLES</span><span>EVERY 18 YEARS</span></div>
    </div>
    <div class="rate-card">
      <div class="head"><span>AGE</span><span class="rate">6%</span></div>
      <div class="rows">
        <div class="row"><span class="age">29</span><span class="amount">$10,000</span></div>
        <div class="row"><span class="age">41</span><span class="amount">$20,000</span></div>
        <div class="row"><span class="age">53</span><span class="amount">$40,000</span></div>
        <div class="row"><span class="age">65</span><span class="amount">$80,000</span></div>
      </div>
      <div class="note"><span>MONEY DOUBLES</span><span>EVERY 12 YEARS</span></div>
    </div>
    <div class="rate-card">
      <div class="head"><span>AGE</span><span class="rate">8%</span></div>
      <div class="rows">
        <div class="row"><span class="age">29</span><span class="amount">$10,000</span></div>
        <div class="row"><span class="age">38</span><span class="amount">$20,000</span></div>
        <div class="row"><span class="age">47</span><span class="amount">$40,000</span></div>
        <div class="row"><span class="age">56</span><span class="amount">$80,000</span></div>
        <div class="row"><span class="age">65</span><span class="amount">$160,000</span></div>
      </div>
      <div class="note"><span>MONEY DOUBLES</span><span>EVERY 9 YEARS</span></div>
    </div>
    <div class="rate-card">
      <div class="head"><span>AGE</span><span class="rate">12%</span></div>
      <div class="rows">
        <div class="row"><span class="age">29</span><span class="amount">$10,000</span></div>
        <div class="row"><span class="age">35</span><span class="amount">$20,000</span></div>
        <div class="row"><span class="age">41</span><span class="amount">$40,000</span></div>
        <div class="row"><span class="age">47</span><span class="amount">$80,000</span></div>
        <div class="row"><span class="age">53</span><span class="amount">$160,000</span></div>
        <div class="row"><span class="age">59</span><span class="amount">$320,000</span></div>
        <div class="row"><span class="age">65</span><span class="amount">$640,000</span></div>
      </div>
      <div class="note"><span>MONEY DOUBLES</span><span>EVERY 6 YEARS</span></div>
    </div>
  </section>

  <h2 class="section-bar taxes">TAXES</h2>

  <svg class="roof" width="810" height="70" viewBox="0 0 810 70" aria-hidden="true">
    <polygon points="405,0 810,66 0,66" fill="var(--navy)"/>
    <polygon points="405,14 740,66 70,66" fill="var(--green)"/>
  </svg>

  <section class="pillars">
    <article class="pillar">
      <h3 class="pillar-title">HOME</h3>
      <ul class="pillar-points">
        <li>Partner with mortgage<br>brokers for best rates</li>
        <li>Mortgage insurance<br>alternatives</li>
      </ul>
      <p class="verdict">SELL</p>
    </article>
    <article class="pillar">
      <h3 class="pillar-title">RRSP</h3>
      <ul class="pillar-points">
        <li>Tax deduction</li>
        <li>Tax deferred</li>
      </ul>
      <p class="verdict">100% TAX</p>
    </article>
    <article class="pillar">
      <h3 class="pillar-title">TFSA</h3>
      <ul class="pillar-points">
        <li>No tax deductions</li>
        <li>Tax free growth</li>
        <li>2009 - $95,000</li>
        <li>Limit 2023 - $7,000/yr</li>
      </ul>
      <p class="verdict">0% TAX</p>
    </article>
    <article class="pillar">
      <h3 class="pillar-title">PERM LIFE</h3>
      <ul class="pillar-points">
        <li>No tax deductions</li>
        <li>Qualify</li>
        <li>Tax deferred growth</li>
      </ul>
      <p class="verdict">0% TAX</p>
    </article>
  </section>

  <div class="foundation">
    <div class="col"><span>LIFE INSURANCE LINES</span><span>CRITICAL / DISABILITY</span></div>
    <div class="col"><span>DEBT MANAGEMENT</span><span>CASH FLOW</span></div>
  </div>
</main>
</body>
</html>
```